Bref créative
Corporate Advisory
Professional
Dorian Pelhame
Director
Suite 14, 88 Calloway Road, Ardenvale. NSW 2719
dorian.pelhame@veltrina.com.au
www.veltrina.com.au
Corporate colours are the blue and white in logo. Front may be one colour eg white with blue logo and rear may be blue with white logo
Can be as simple as blue background and white logo
Veltrina logo - white background with blue logo is primary and blue background with white logo is secondary - no other coloures used.

```html
<!DOCTYPE html>
<html lang="en">
<head>
<meta charset="utf-8">
<title>Veltrina Stationery</title>
<link href="https://fonts.googleapis.com/css2?family=Raleway:wght@300;400;500&display=swap" rel="stylesheet">
<style>
  :root {
    --navy: #24395a;
    --white: #ffffff;
    --backdrop: #e6e7ea;
    --ink-soft: #4a5a73;
    --faint: #dfe3ea;
  }
  * { margin: 0; padding: 0; box-sizing: border-box; }
  html, body { width: 1200px; height: 1000px; overflow: hidden; }
  body {
    background: var(--backdrop);
    font-family: "Raleway", Arial, sans-serif;
    color: var(--navy);
    position: relative;
  }
  .sheet { position: absolute; background: var(--white); box-shadow: 0 2px 8px rgba(0,0,0,.12); overflow: hidden; }

  /* brand lockup */
  .brand { display: flex; align-items: center; gap: 14px; }
  .brand-square { background: var(--navy); flex: none; }
  .brand-name { font-weight: 300; letter-spacing: .06em; line-height: 1; white-space: nowrap; }
  .tagline { font-weight: 400; letter-spacing: .08em; text-transform: uppercase; white-space: nowrap; }

  /* letterhead */
  .letterhead { left: 27px; top: 180px; width: 612px; height: 785px; }
  .letterhead .brand { position: absolute; left: 76px; top: 30px; }
  .letterhead .brand-square { width: 54px; height: 54px; }
  .letterhead .brand-name { font-size: 60px; }
  .letterhead .tagline { position: absolute; left: 76px; top: 96px; font-size: 12.5px; }
  .letterhead .rule { position: absolute; left: 0; right: 0; top: 134px; height: 2px; background: var(--navy); }
  .letterhead .watermark { position: absolute; left: 459px; top: 570px; width: 120px; height: 180px; background: var(--faint); }
  .letterhead .footer { position: absolute; left: 28px; bottom: 14px; font-size: 10.5px; color: var(--ink-soft); white-space: nowrap; }

  /* envelope */
  .envelope { left: 486px; top: 359px; width: 654px; height: 376px; }
  .envelope .flap { position: absolute; left: 0; top: 0; }
  .envelope .flap-mark { position: absolute; left: 316px; top: 56px; width: 22px; height: 22px; background: var(--white); }
  .envelope .brand { position: absolute; left: 30px; top: 118px; }
  .envelope .brand-square { width: 38px; height: 38px; }
  .envelope .brand-name { font-size: 46px; }
  .envelope .tagline { position: absolute; left: 30px; top: 170px; font-size: 10px; }
  .envelope .return-address { position: absolute; left: 30px; top: 188px; font-size: 9.5px; color: var(--ink-soft); white-space: nowrap; }
  .envelope .base-band { position: absolute; left: 0; right: 0; bottom: 0; height: 28px; background: var(--navy); }
  .envelope .base-band .web { position: absolute; right: 16px; top: 9px; font-size: 9px; color: var(--white); }

  /* business cards */
  .card { top: 73px; width: 240px; height: 132px; }
  .card-front { left: 656px; }
  .card-front .brand { position: absolute; left: 14px; top: 12px; gap: 8px; }
  .card-front .brand-square { width: 20px; height: 20px; }
  .card-front .brand-name { font-size: 25px; }
  .card-front .tagline { position: absolute; left: 14px; top: 38px; font-size: 5.5px; }
  .card-front .details { position: absolute; left: 14px; top: 52px; font-size: 6.5px; line-height: 1.45; color: var(--ink-soft); white-space: nowrap; }
  .card-front .details .person { font-size: 8px; font-weight: 500; color: var(--navy); text-transform: uppercase; }
  .card-back { left: 926px; background: var(--navy); }
  .card-back .back-square { position: absolute; left: 172px; top: 16px; width: 44px; height: 44px; background: var(--white); }
  .card-back .web { position: absolute; right: 12px; bottom: 12px; font-size: 7px; color: var(--white); }
</style>
</head>
<body>

  <section class="sheet letterhead">
    <div class="brand">
      <span class="brand-square"></span>
      <span class="brand-name">VELTRINA</span>
    </div>
    <p class="tagline">Considered advice, clearly given</p>
    <div class="rule"></div>
    <div class="watermark"></div>
    <p class="footer">Suite 14, 88 Calloway Road, Ardenvale. NSW 2719 &bull; P: +61 2 5550 0142 &bull; F: +61 2 5550 0143 &bull; www.veltrina.com.au</p>
  </section>

  <section class="sheet envelope">
    <svg class="flap" width="654" height="100" viewBox="0 0 654 100">
      <path d="M0 0 H654 V58 Q654 74 636 74 H361 L327 98 L293 74 H18 Q0 74 0 58 Z" fill="var(--navy)"/>
    </svg>
    <span class="flap-mark"></span>
    <div class="brand">
      <span class="brand-square"></span>
      <span class="brand-name">VELTRINA</span>
    </div>
    <p class="tagline">Considered advice, clearly given</p>
    <p class="return-address">Suite 14, 88 Calloway Road, Ardenvale. NSW 2719</p>
    <div class="base-band"><span class="web">www.veltrina.com.au</span></div>
  </section>

  <section class="sheet card card-front">
    <div class="brand">
      <span class="brand-square"></span>
      <span class="brand-name">VELTRINA</span>
    </div>
    <p class="tagline">Considered advice, clearly given</p>
    <div class="details">
      <p class="person">Dorian Pelhame</p>
      <p>Director</p>
      <p>P: +61 2 5550 0142</p>
      <p>M: 0455 018 274</p>
      <p>F: +61 2 5550 0143</p>
      <p>E: dorian.pelhame@veltrina.com.au</p>
    </div>
  </section>

  <section class="sheet card card-back">
    <span class="back-square"></span>
    <span class="web">www.veltrina.com.au</span>
  </section>

</body>
</html>
```